Tequila Bottle Labels

We are a construction company that bottled our own tequila and would like a unique label for it! We already have our own company logo (linked below) and we want that logo somewhere on the bottle as well- it can be big or small. It was brewed & bottled in Southern California. Ideally it would have the year "2020," "Single Estate," & "100% Agave Azul" somewhere on the label.

Logo Text

Tequila / MTR / 2020

```html
<!DOCTYPE html>
<html lang="en">
<head>
<meta charset="utf-8">
<title>MTR Tequila 2020 — Bottle Label</title>
<link rel="stylesheet" href="https://fonts.googleapis.com/css2?family=Alfa+Slab+One&family=Oswald:wght@600&family=Open+Sans:wght@800&display=swap">
<style>
  :root {
    --backdrop: #9a9a9a;
    --label-light: #e3a300;
    --label-dark: #c98a00;
    --ink: #141008;
  }
  * { margin: 0; padding: 0; box-sizing: border-box; }
  html, body {
    width: 1200px;
    height: 1027px;
    overflow: hidden;
    background: var(--backdrop);
  }
  .label {
    position: absolute;
    left: 180px;
    top: 64px;
    width: 840px;
    height: 900px;
    background: linear-gradient(90deg, var(--label-dark) 0%, var(--label-light) 55%, var(--label-dark) 100%);
    overflow: hidden;
    color: var(--ink);
  }
  .label__title {
    position: absolute;
    top: 160px;
    left: 0;
    width: 100%;
    text-align: center;
    font-family: "Alfa Slab One", serif;
    font-size: 150px;
    line-height: 1;
    letter-spacing: 4px;
  }
  .label__year {
    position: absolute;
    top: 350px;
    left: 0;
    width: 100%;
    text-align: center;
    font-family: "Oswald", sans-serif;
    font-weight: 600;
    font-size: 62px;
    line-height: 1;
  }
  .specs {
    position: absolute;
    top: 470px;
    left: 90px;
    width: 640px;
    height: 100px;
    font-family: "Open Sans", sans-serif;
    font-weight: 800;
    font-size: 17px;
    text-transform: uppercase;
  }
  .specs__item { position: absolute; white-space: nowrap; }
  .specs__item--origin { right: 340px; top: 8px; }
  .specs__item--estate { left: 320px; top: 8px; }
  .specs__item--agave { right: 340px; top: 66px; }
  .specs__item--abv { left: 320px; top: 66px; }
  .specs__rule-h {
    position: absolute;
    left: 80px;
    right: 0;
    top: 50px;
    height: 3px;
    background: var(--ink);
  }
  .specs__rule-v {
    position: absolute;
    left: 300px;
    top: 0;
    width: 3px;
    height: 100px;
    background: var(--ink);
  }
  .label__skyline {
    position: absolute;
    left: 0;
    bottom: 0;
    width: 100%;
    height: 340px;
  }
  .label__brand {
    position: absolute;
    left: 0;
    bottom: -30px;
    width: 100%;
    text-align: center;
    font-family: "Alfa Slab One", serif;
    font-size: 300px;
    line-height: 1;
    letter-spacing: -6px;
  }
</style>
</head>
<body>
  <section class="label">
    <h1 class="label__title">TEQUILA</h1>
    <p class="label__year">2020</p>

    <div class="specs">
      <span class="specs__item specs__item--origin">Brewed &amp; bottled in S.California</span>
      <span class="specs__item specs__item--estate">Single Estate</span>
      <span class="specs__item specs__item--agave">100% Agave Azul</span>
      <span class="specs__item specs__item--abv">40% Alc . 750ml</span>
      <div class="specs__rule-h"></div>
      <div class="specs__rule-v"></div>
    </div>

    <svg class="label__skyline" viewBox="0 0 840 340" role="img" aria-label="Silhouette of a city skyline with construction cranes along the bottom edge">
      <defs>
        <linearGradient id="skylineFade" x1="0" y1="0" x2="0" y2="1">
          <stop offset="0" stop-color="#141008" stop-opacity="0"/>
          <stop offset="0.75" stop-color="#141008" stop-opacity="0.15"/>
          <stop offset="1" stop-color="#141008" stop-opacity="0.85"/>
        </linearGradient>
      </defs>
      <rect x="0" y="0" width="840" height="340" fill="url(#skylineFade)"/>
    </svg>

    <div class="label__brand">MTR</div>
  </section>
</body>
</html>
```